International Student Travel Company needs a web page re-designed

Pellham Journeys is a worldwide leader in student educational and performing arts travel programs. We provide high-quality tours that exceed the expectations of our participants/customers and enhance a student's learning experiences. Our mission is to forever change how every student sees the world around them. Our company has 3 distinct brands: Pellham Journeys (www.pellhamjourneys.example), Brightwell Voyages (www.brightwellvoyages.example) and Northfield Heritage Trips & Band Jamborees (www.nfheri.example).

As part of our travel programs, we offer participants the option to purchase travel insurance. We are looking to re-design the page that offers each participant the option to buy insurance during their online registration process to maximize the number of customers who purchase the recommended option. The registration process is set up behind a password protected registration website.

Here is a link to view the current page for each brand:
https://accounts.pellhamjourneys.example/tech/demo/3172
https://accounts.brightwellvoyages.example/tech/demo/3172
https://accounts.nfheri.example/tech/demo/3172

We are attaching the HTML for the current page so you can start with the current format that this design is a part of- for example, the header & footer and the "Registration Step # section".

Please note that this current design was created for the "Brightwell Voyages" brand as you may note the use of the orange color on the page. We would like to design the page so that we can easily implement the same design for all 3 brands. As you will see from looking at the brands online, they all share a similar blue that can be used where we need a color as you will see on our SAMPLE mock-up that we have included as an attachment.

In our SAMPLE mock-up (file attached named "SAMPLE webpage mock-up.pdf") we have icons at the top of the insurance option which is meant to be a link to a PDF that is an advertisement for each type of travel insurance. So, however you decide to design that element, please make sure to include that as a link that will open a PDF in a new tab. The "None" option will open up the PDF attached named "Note to Parents.pdf". The "Scholar Shield" option will open up the PDF attached named "Marlow & Pike.pdf". The "Scholar Shield with CFAR" option will open up the PDF attached named "CFAR.pdf".

The sample mock-up is just a sample draft idea of how we would want it to look. Please feel free to re-design completely or as close to this design as you wish using your best design judgment. The goal is to make it look very professional and convince customers to select the recommended "Scholar Shield with CFAR" option as this will fully protect them in case they need to cancel.

It is very important to use all the copy as its presented since the language has all been approved by the insurance company's compliance team.

*VERY IMPORTANT*
Please design this so that it is MOBILE friendly. Many of our customers register for our trips on their mobile devices. So, because we are presenting 3 options to compare we need to make sure the design works well on small mobile screens. So, please present your designs for both large computer screens and small mobile devices so we can see how it would look at the various different screen sizes.

Please let us know if you have any questions or require any more info from us to get started. We are looking forward to seeing your designs!

-Pellham Journeys Marketing Team

```html
<!DOCTYPE html>
<html lang="en">
<head>
<meta charset="utf-8">
<title>Registration – Travel Protection Options</title>
<link href="https://fonts.googleapis.com/css2?family=Lato:ital,wght@0,400;0,700;0,900;1,400&family=Montserrat:wght@700;800;900&family=Titillium+Web:wght@400;600&display=swap" rel="stylesheet">
<style>
:root{
  --brand-blue:#1d5cab;
  --tab-blue:#1c5aa8;
  --sky:#35a9ef;
  --ink:#222;
  --text:#555;
  --muted:#777;
  --lavender:#adb7de;
  --lavender-soft:#f1f3fa;
  --line:#d9def0;
  --red:#d8232c;
  --green:#3c9d2a;
  --footer:#2a2a2a;
}
*{box-sizing:border-box;margin:0;padding:0}
html,body{width:1200px;height:3592px;overflow:hidden}
body{position:relative;background:#fff;font-family:"Lato",sans-serif;color:var(--text)}
a{text-decoration:none;color:inherit}
.abs{position:absolute}

/* header */
.site-header{left:0;top:0;width:1200px;height:98px;border-bottom:1px solid #cfd3dc}
.brand{left:112px;top:26px;display:flex;align-items:center;gap:10px}
.brand-mark{width:18px;height:18px;border-radius:50%;background:var(--brand-blue)}
.brand-name{font-weight:900;font-size:23px;color:var(--brand-blue);letter-spacing:.3px}
.account{left:669px;top:20px;display:flex;align-items:center;gap:14px}
.avatar{width:58px;height:58px;border-radius:50%;background:#b9bcc4}
.account-text{font-size:16px;color:#333;line-height:23px}
.account-text strong{font-size:19px;font-weight:400}
.btn-logout{left:951px;top:22px;width:136px;height:52px;border-radius:26px;background:var(--sky);color:#fff;font-weight:700;font-size:17px;display:flex;align-items:center;justify-content:center;gap:6px}

/* registration */
.reg-title{left:112px;top:126px;font-family:"Montserrat",sans-serif;font-weight:900;font-size:38px;color:var(--ink)}
.reg-step{right:113px;top:128px;font-family:"Titillium Web",sans-serif;font-size:27px;color:#222}
.reg-step span{color:var(--sky)}
.tour-info{left:112px;top:194px;width:975px;height:147px;border:1px solid #cfd3dc;border-radius:14px;padding:20px 27px;font-size:16px}
.tour-info h2{font-weight:400;font-size:19px;color:#444;margin-bottom:18px}
.tour-grid{display:grid;grid-template-columns:137px 283px 140px 1fr;row-gap:10px}
.tour-grid dt{color:#666}
.tour-grid dd{color:#333;font-weight:700;font-size:16px}

/* hero */
.hero{left:0;top:383px;width:1200px;height:531px;background:linear-gradient(180deg,#3f7fca 0%,#7fb0dc 55%,#c9c9c6 82%,#6f9b4c 100%)}
.hero-photo{left:0;top:0;width:640px;height:531px;background:linear-gradient(90deg,#d9a88a 0%,#c88c7a 40%,rgba(120,140,180,0) 100%)}
.hero-title{left:672px;top:100px;font-family:"Montserrat",sans-serif;font-weight:900;font-size:64px;line-height:78px;color:#fff;letter-spacing:1px}
.hero-note{left:112px;top:841px;width:975px;height:144px;background:var(--brand-blue);color:#fff;font-style:italic;font-size:21px;line-height:35px;text-align:center;padding-top:20px;box-shadow:0 16px 20px -12px rgba(0,0,0,.35)}

/* protect */
.protect-title{left:109px;top:1046px;font-family:"Montserrat",sans-serif;font-weight:900;font-size:46px;line-height:62px;color:var(--ink)}
.protect-copy{left:109px;top:1190px;width:570px;font-size:17px;line-height:32px;color:#555}
.protect-copy p+p{margin-top:31px}
.protect-copy strong{color:#222;font-weight:700}
.partner-ring{left:736px;top:1049px;width:320px;height:320px;border-radius:50%;border:10px solid #d6dbee;background:#fff;display:flex;align-items:center;justify-content:center;gap:10px}
.partner-ring::after{content:"";position:absolute;left:40px;bottom:-40px;width:240px;height:18px;border-radius:50%;background:rgba(0,0,0,.08);filter:blur(6px)}
.partner-mark{width:22px;height:22px;background:var(--brand-blue)}
.partner-name{font-weight:900;font-size:19px;color:#222}

/* cost band */
.cost-band{left:0;top:1499px;width:1200px;height:341px;background:var(--lavender)}
.cost-title{left:0;top:1546px;width:1200px;text-align:center;font-family:"Montserrat",sans-serif;font-weight:800;font-size:37px;color:#fff}
.cost-sub{left:0;top:1610px;width:1200px;text-align:center;font-family:"Titillium Web",sans-serif;font-size:31px;color:#fff}

/* plans */
.plan{top:1763px;width:235px;height:478px;background:#fff;border:1px solid var(--line);border-bottom:none;border-radius:12px 12px 0 0;text-align:center}
.plan-tab{position:absolute;left:29px;top:-30px;width:177px;height:47px;background:var(--tab-blue);color:#fff;font-family:"Titillium Web",sans-serif;font-size:20px;line-height:20px;display:flex;align-items:center;justify-content:center;text-align:center}
.plan-tab.two{font-size:19px;line-height:20px}
.plan-info{position:absolute;right:-4px;top:-10px;width:18px;height:18px;border-radius:50%;background:#e4e6ee;color:#444;font-size:11px;font-weight:700;display:flex;align-items:center;justify-content:center}
.plan-price{margin-top:24px;height:36px;font-family:"Montserrat",sans-serif;font-weight:800;font-size:28px;color:#222;display:flex;align-items:center;justify-content:center}
.plan-desc{margin:10px 12px 0;height:70px;font-family:"Titillium Web",sans-serif;font-weight:600;font-size:17px;line-height:24px;color:#333}
.plan-desc em{font-weight:400}
.plan hr{border:none;border-top:1px solid var(--line);margin:4px 14px 0}
.plan-feats{list-style:none;text-align:left;padding:16px 12px 0 14px;font-size:13.5px;line-height:14.5px;color:#666}
.plan-feats li{display:flex;gap:7px;margin-bottom:14px}
.plan-feats li svg{flex:none;margin-top:2px}
.plan-feats li.no{color:var(--red)}
.plan-feats li.yes{color:var(--green)}
.plan-feats li.sub{padding-left:22px}
.plan-select{position:absolute;left:66px;top:415px;width:102px;height:38px;border-radius:19px;background:var(--sky);color:#fff;font-weight:700;font-size:14px;display:flex;align-items:center;justify-content:center;letter-spacing:.3px}
.ribbon{left:875px;top:1676px;width:196px;height:43px;background:var(--red);color:#ffe14a;font-size:16px;display:flex;align-items:center;justify-content:center;gap:8px;clip-path:polygon(0 0,100% 0,93% 50%,100% 100%,0 100%,7% 50%)}

/* table */
.benefits{left:112px;top:2241px;width:975px;border:1px solid var(--line);border-radius:0 0 10px 10px;overflow:hidden}
.benefits-row{display:grid;grid-template-columns:245px 245px 245px 1fr;height:57.2px;border-top:1px solid var(--line)}
.benefits-row:nth-child(even){background:var(--lavender-soft)}
.benefits-row>div{display:flex;align-items:center;justify-content:center;text-align:center;font-size:16px;line-height:18px;color:#555;border-left:1px solid var(--line);padding:0 6px}
.benefits-row>div:first-child{border-left:none}
.benefits-head{height:56px;background:var(--lavender);border-top:none}
.benefits-head>div{color:#fff;font-family:"Titillium Web",sans-serif;font-size:23px;border-left-color:#c6ceea}
.benefits-row .cfar{color:var(--green);font-weight:700;font-size:15px;letter-spacing:.3px}
.benefits-tab{left:127px;top:2230px;width:219px;height:57px;background:var(--tab-blue);color:#fff;font-family:"Titillium Web",sans-serif;font-size:20px;display:flex;align-items:center;justify-content:center;box-shadow:0 10px 12px -8px rgba(0,0,0,.4);z-index:2}

/* notes */
.notes{left:112px;top:2953px;width:965px;font-size:16px;line-height:24px;color:#555}
.notes p{margin-bottom:24px}
.notes strong{color:#333}
.limits-link{left:112px;top:3300px;font-size:17px;font-weight:700;color:var(--sky);text-decoration:underline;letter-spacing:.2px}
.plan-code{left:110px;top:3333px;font-size:18px;color:var(--sky)}
.btn-back{left:623px;top:3346px;width:144px;height:54px;border:2px solid var(--sky);border-radius:27px;color:var(--sky);font-weight:700;font-size:17px;display:flex;align-items:center;justify-content:center}
.btn-continue{left:778px;top:3346px;width:307px;height:54px;border-radius:27px;background:var(--sky);color:#fff;font-weight:700;font-size:17px;display:flex;align-items:center;justify-content:center}

/* footer */
.site-footer{left:0;top:3471px;width:1200px;height:121px;background:var(--footer);color:#eee;text-align:center;font-size:16px}
.site-footer p{margin-top:36px}
.footer-links{margin-top:12px;display:flex;justify-content:center;align-items:center;gap:14px}
</style>
</head>
<body>

<header class="site-header abs">
  <div class="brand abs">
    <span class="brand-mark"></span><span class="brand-name">Brightwell Voyages</span>
  </div>
  <div class="account abs">
    <span class="avatar"></span>
    <div class="account-text">Signed on as<br><strong>webuser@mail.example</strong></div>
  </div>
  <a class="btn-logout abs" href="#">
    <svg width="14" height="14" viewBox="0 0 14 14"><rect x="1" y="6" width="10" height="8" rx="1" fill="#fff"/><path d="M4 6V4a3 3 0 0 1 6 0" stroke="#fff" stroke-width="1.8" fill="none"/></svg>LOGOUT
  </a>
</header>

<h1 class="reg-title abs">REGISTRATION</h1>
<div class="reg-step abs"><span>Step 7</span>/8: Travel Protection Options</div>

<section class="tour-info abs">
  <h2>YOUR TOUR INFORMATION :</h2>
  <dl class="tour-grid">
    <dt>Group Name:</dt><dd>Lakeview Elementary School</dd><dt>Tour Dates:</dt><dd>3/2/2021</dd>
    <dt>Tour Name:</dt><dd>Two Days Test Tour</dd><dt>Tour Organizer:</dt><dd>Mr. Dalton Reese</dd>
  </dl>
</section>

<section class="hero abs">
  <div class="hero-photo abs" role="img" aria-label="Group of smiling students with a map in front of the Capitol building"></div>
  <div class="hero-title abs">TRAVEL<br>PAYMENT<br>PROTECTION</div>
</section>
<div class="hero-note abs">Travel Insurance is optional, but unexpected events are always a possibility...<br>and without the Scholar Shield Group Travel Protection, you might lose up<br>to 100% of your trip investment.</div>

<h2 class="protect-title abs">PROTECT YOUR<br>TRIP INVESTMENT!</h2>
<div class="protect-copy abs">
  <p>Harborline Travel Cover, a leading provider of group travel insurance, offers participants the opportunity to protect their travel investment.</p>
  <p>This program offers an array of <strong>travel protection</strong> benefits including 24/7 Worldwide Non-Insurance Assistance Services as well as Trip Cancellation, Trip Interruption, Medical Expense, Baggage and Personal Effects, and more travel insurance coverages such as the Cancel for Any Reason (CFAR) option, if eligible.</p>
</div>
<div class="partner-ring abs"><span class="partner-mark"></span><span class="partner-name">Harborline Travel Cover</span></div>

<div class="cost-band abs"></div>
<div class="cost-title abs">To Start, Please Enter Your Total Trip Cost: $______</div>
<div class="cost-sub abs">Enter Total Trip Cost Above</div>

<div class="ribbon abs">
  <svg width="14" height="14" viewBox="0 0 10 10"><path d="M5 0l1.5 3.2 3.5.4-2.6 2.4.7 3.5L5 7.8 1.9 9.5l.7-3.5L0 3.6l3.5-.4z" fill="#ffe14a"/></svg>Recommended<svg width="14" height="14" viewBox="0 0 10 10"><path d="M5 0l1.5 3.2 3.5.4-2.6 2.4.7 3.5L5 7.8 1.9 9.5l.7-3.5L0 3.6l3.5-.4z" fill="#ffe14a"/></svg>
</div>

<article class="plan abs" style="left:362px">
  <a class="plan-tab" href="#" target="_blank">None</a><span class="plan-info">?</span>
  <div class="plan-price"><svg width="22" height="22" viewBox="0 0 10 10"><path d="M1.5 1.5l7 7M8.5 1.5l-7 7" stroke="#d8232c" stroke-width="2.2"/></svg></div>
  <p class="plan-desc">Potentially lose 100% of your tour cost</p>
  <hr>
  <ul class="plan-feats">
    <li><svg width="11" height="11" viewBox="0 0 10 10"><path d="M1 5l3 3 5-6" stroke="#666" stroke-width="2" fill="none"/></svg>No Payment Protection</li>
  </ul>
  <a class="plan-select" href="#">SELECT</a>
</article>

<article class="plan abs" style="left:608px">
  <a class="plan-tab" href="#" target="_blank">Scholar Shield</a><span class="plan-info">?</span>
  <div class="plan-price">$100</div>
  <p class="plan-desc">Protects your trip investment for covered reasons only</p>
  <hr>
  <ul class="plan-feats">
    <li><svg width="11" height="11" viewBox="0 0 10 10"><path d="M1 5l3 3 5-6" stroke="#666" stroke-width="2" fill="none"/></svg>Trip Cancellation coverage provides a 100% refund if you need to cancel for covered reasons</li>
    <li><svg width="11" height="11" viewBox="0 0 10 10"><path d="M1 5l3 3 5-6" stroke="#666" stroke-width="2" fill="none"/></svg>Includes additional coverages as per below Schedule</li>
    <li class="no"><svg width="11" height="11" viewBox="0 0 10 10"><path d="M1.5 1.5l7 7M8.5 1.5l-7 7" stroke="#d8232c" stroke-width="2.2"/></svg>Does NOT include Cancel for Any Reason (CFAR)***</li>
    <li class="no sub"><svg width="11" height="11" viewBox="0 0 10 10"><path d="M1.5 1.5l7 7M8.5 1.5l-7 7" stroke="#d8232c" stroke-width="2.2"/></svg>No coverage for cancellations due to fear of a pandemic</li>
  </ul>
  <a class="plan-select" href="#">SELECT</a>
</article>

<article class="plan abs" style="left:852px">
  <a class="plan-tab two" href="#" target="_blank">Scholar Shield<br>with CFAR</a><span class="plan-info">?</span>
  <div class="plan-price">$150</div>
  <p class="plan-desc">Protects your trip investment if you need to cancel for <em>any reason</em>***</p>
  <hr>
  <ul class="plan-feats">
    <li><svg width="11" height="11" viewBox="0 0 10 10"><path d="M1 5l3 3 5-6" stroke="#666" stroke-width="2" fill="none"/></svg>Trip Cancellation coverage provides a 100% refund if you need to cancel for covered reasons</li>
    <li><svg width="11" height="11" viewBox="0 0 10 10"><path d="M1 5l3 3 5-6" stroke="#666" stroke-width="2" fill="none"/></svg>Includes additional coverages as per below Schedule</li>
    <li class="yes"><svg width="11" height="11" viewBox="0 0 10 10"><path d="M1 5l3 3 5-6" stroke="#3c9d2a" stroke-width="2" fill="none"/></svg>Includes Cancel for Any Reason (CFAR)***</li>
    <li class="yes sub"><svg width="11" height="11" viewBox="0 0 10 10"><path d="M1 5l3 3 5-6" stroke="#3c9d2a" stroke-width="2" fill="none"/></svg>Covers cancellations due to fear of a pandemic</li>
  </ul>
  <a class="plan-select" href="#">SELECT</a>
</article>

<div class="benefits-tab abs">Benefits</div>
<section class="benefits abs">
  <div class="benefits-row benefits-head"><div></div><div>Maximum Limit</div><div>Maximum Limit</div><div>Maximum Limit</div></div>
  <div class="benefits-row"><div class="cfar">CANCEL FOR<br>ANY REASON (CFAR)***</div><div><svg width="13" height="13" viewBox="0 0 10 10"><path d="M1.5 1.5l7 7M8.5 1.5l-7 7" stroke="#d8232c" stroke-width="2.2"/></svg></div><div><svg width="13" height="13" viewBox="0 0 10 10"><path d="M1.5 1.5l7 7M8.5 1.5l-7 7" stroke="#d8232c" stroke-width="2.2"/></svg></div><div class="cfar">CANCEL FOR ANY REASON<br>(CFAR)***: INCLUDED</div></div>
  <div class="benefits-row"><div>Trip Cancellation**</div><div><svg width="13" height="13" viewBox="0 0 10 10"><path d="M1.5 1.5l7 7M8.5 1.5l-7 7" stroke="#d8232c" stroke-width="2.2"/></svg></div><div>Trip Cost*</div><div>Trip Cost*</div></div>
  <div class="benefits-row"><div>Trip Interruption**</div><div><svg width="13" height="13" viewBox="0 0 10 10"><path d="M1.5 1.5l7 7M8.5 1.5l-7 7" stroke="#d8232c" stroke-width="2.2"/></svg></div><div>150% Trip Cost</div><div>150% of Trip Cost</div></div>
  <div class="benefits-row"><div>Travel Delay – 6 Hours</div><div><svg width="13" height="13" viewBox="0 0 10 10"><path d="M1.5 1.5l7 7M8.5 1.5l-7 7" stroke="#d8232c" stroke-width="2.2"/></svg></div><div>$750 ($150/day)</div><div>$750 ($150/day)</div></div>
  <div class="benefits-row"><div>Missed Connection – 3 Hours</div><div><svg width="13" height="13" viewBox="0 0 10 10"><path d="M1.5 1.5l7 7M8.5 1.5l-7 7" stroke="#d8232c" stroke-width="2.2"/></svg></div><div>$500</div><div>$500</div></div>
  <div class="benefits-row"><div>Baggage/Personal Effects</div><div><svg width="13" height="13" viewBox="0 0 10 10"><path d="M1.5 1.5l7 7M8.5 1.5l-7 7" stroke="#d8232c" stroke-width="2.2"/></svg></div><div>$1,500</div><div>$1,500</div></div>
  <div class="benefits-row"><div>Baggage Delay – 24 Hours</div><div><svg width="13" height="13" viewBox="0 0 10 10"><path d="M1.5 1.5l7 7M8.5 1.5l-7 7" stroke="#d8232c" stroke-width="2.2"/></svg></div><div>$300</div><div>$300</div></div>
  <div class="benefits-row"><div>Emergency Medical Evacuation, Medical Repatriation &amp; Return of Remains</div><div><svg width="13" height="13" viewBox="0 0 10 10"><path d="M1.5 1.5l7 7M8.5 1.5l-7 7" stroke="#d8232c" stroke-width="2.2"/></svg></div><div>$100,000</div><div>$100,000</div></div>
  <div class="benefits-row"><div>Accident &amp; Sickness<br>Medical Expense</div><div><svg width="13" height="13" viewBox="0 0 10 10"><path d="M1.5 1.5l7 7M8.5 1.5l-7 7" stroke="#d8232c" stroke-width="2.2"/></svg></div><div>$25,000</div><div>$25,000</div></div>
  <div class="benefits-row"><div>Non-Medical Emergency<br>Evacuation</div><div><svg width="13" height="13" viewBox="0 0 10 10"><path d="M1.5 1.5l7 7M8.5 1.5l-7 7" stroke="#d8232c" stroke-width="2.2"/></svg></div><div>$100,00</div><div>$100,00</div></div>
  <div class="benefits-row"><div>Non-Insurance Worldwide Emergency Assistance Services</div><div><svg width="13" height="13" viewBox="0 0 10 10"><path d="M1.5 1.5l7 7M8.5 1.5l-7 7" stroke="#d8232c" stroke-width="2.2"/></svg></div><div>Included</div><div>Included</div></div>
</section>

<section class="notes abs">
  <p>Coverages may vary and not all coverage is available in all jurisdictions. Totals listed below each coverage are the maximum benefit amount payable.</p>
  <p>* Up to the lesser of the Trip Cost paid or the limit of Coverage for which benefits are requested and the appropriate plan cost has been paid. Maximum limit of $10,000</p>
  <p>** For $0 Trip Cost, there is no Trip Cancellation and Trip Interruption is limited to $500 return air only</p>
  <p>*** CFAR coverage is the lessor of 75% of the nonrefundable trip cost or up to the maximum of $10,000. CFAR is optional and available for purchase on an individual level. Trip cancellation must be 48 hours or more prior to scheduled departure. CFAR must be purchased at the time of plan purchase and with, or before your final payment. CFAR is available if you paid your Travel Supplier for the full cost for all non-refundable trip costs for your trip prior to your cancellation of trip. For $0 Trip Cost there is no CFAR. <strong>This benefit is not available to residents of New York State.</strong></p>
</section>
<a class="limits-link abs" href="#">CLICK HERE FOR LIMITATIONS AND EXCLUSIONS AS WELL AS IMPORTANT DISCLAIMERS</a>
<div class="plan-code abs">PX-4817</div>
<a class="btn-back abs" href="#">BACK</a>
<a class="btn-continue abs" href="#">CONTINUE TOUR REGISTRATION</a>

<footer class="site-footer abs">
  <p>© 2020 Brightwell Voyages, Inc. rs, Inc.</p>
  <div class="footer-links">
    <span><svg width="15" height="11" viewBox="0 0 15 11"><rect width="15" height="11" rx="1" fill="#eee"/><path d="M0 1l7.5 5L15 1" stroke="#2a2a2a" stroke-width="1.4" fill="none"/></svg> CONTACT US</span>|
    <span><svg width="12" height="12" viewBox="0 0 12 12"><path d="M2.5 0.5l2 2.6-1.2 1.4a7 7 0 0 0 4.2 4.2l1.4-1.2 2.6 2-1.4 2A9.5 9.5 0 0 1 0.5 1.9z" fill="#eee"/></svg> (800) 555-0147</span>|
    <span>Privacy Policy</span>|
    <span>Responsibility</span>
  </div>
</footer>

</body>
</html>
```